Kovrix - consultancy website

I need a new design for my webpage/presence [to be functioning with Wordpress - I have a programmer to set it up but not the design idea].
My company is Kovrix - a consultancy firm focused on growth management for Swedish SME's primarily;. We call it Leadership add-on for firms on the rise, kind of a doctor helping small become big. Contentwise, its a simple frontpage + 3-4 subpages with content re company/myself/focus etc. The new site should communicate a fresh, trustworthy take yet simple and functional on all devices [i.e. think UI compatible for mobile/tablet]. Current building parts/form elements are
a) existing logo and text elements
b) existing pictures
c) the yellowish color
colours and new ideas on pictures/positioning are welcome. I prefer a 'full width page' solution with centralised text elements but that's all up to you to suggest. Current site is a quickfix made by myself - now I'm moving it to a new platform so want to take the opportunity to make it
Nothing superspecial as it is a 2-man show; on the other hand I still want to have a modern & fresh reflection of my brand in digital environments. Help me out!
www.kovrix-demo.se
Best
Lotta Bergqvalm

```html
<!DOCTYPE html>
<html lang="en">
<head>
<meta charset="utf-8">
<title>Kovrix – Consultancy</title>
<link rel="stylesheet" href="https://fonts.googleapis.com/css2?family=Raleway:wght@300;400;500&family=Open+Sans:wght@400;600&display=swap">
<style>
  :root{
    --brand-blue:#3868dc;
    --footer-blue:#1b52da;
    --nav-active:#2c3140;
    --heading-blue:#4a7ce0;
    --text-dark:#2a2a2a;
    --highlight-yellow:#fbf22c;
    --link-orange:#e4510c;
    --white:#ffffff;
    --hero-dark:#1c1f24;
  }
  *{margin:0;padding:0;box-sizing:border-box;}
  html,body{width:1200px;height:2488px;overflow:hidden;background:var(--white);}
  body{position:relative;font-family:"Open Sans",Arial,sans-serif;color:var(--text-dark);}

  .site-header{position:absolute;left:0;top:0;width:1200px;height:192px;background:var(--brand-blue);overflow:hidden;}
  .brand-name{position:absolute;left:36px;top:54px;font-family:"Raleway",sans-serif;font-weight:400;font-size:70px;color:var(--white);letter-spacing:1px;}
  .main-nav{position:absolute;left:572px;top:0;height:192px;display:flex;}
  .nav-item{height:192px;display:flex;align-items:center;font-family:"Open Sans",sans-serif;font-size:31px;color:var(--white);white-space:nowrap;padding:0 32px;}
  .nav-item.is-active{background:var(--nav-active);width:220px;justify-content:center;padding:0;}

  .hero{position:absolute;left:0;top:192px;width:1200px;height:780px;}
  .hero-visual{position:absolute;inset:0;background:radial-gradient(ellipse at 62% 45%,#3b4a5c 0%,#23282f 45%,var(--hero-dark) 100%);}
  .hero-tagline{position:absolute;left:20px;top:186px;width:560px;font-family:"Raleway",sans-serif;font-weight:400;font-size:41px;line-height:56px;color:var(--white);}

  .intro{position:absolute;left:0;top:972px;width:1200px;}
  .section-title{font-family:"Raleway",sans-serif;font-weight:300;font-size:68px;color:var(--heading-blue);text-align:center;}
  .intro .section-title{position:absolute;top:76px;width:1200px;}
  .intro-body{position:absolute;left:132px;top:206px;width:1000px;}
  .intro-copy{font-size:20px;line-height:30px;white-space:nowrap;margin-bottom:30px;}

  .offer-band{position:absolute;left:0;top:1520px;width:1200px;height:116px;background:var(--highlight-yellow);display:flex;align-items:center;justify-content:center;font-size:30px;color:var(--text-dark);}
  .offer-band a{color:var(--link-orange);text-decoration:underline;margin-left:10px;}
  .offer-corner{position:absolute;left:0;top:1490px;}

  .expertise .section-title{position:absolute;top:1716px;width:1200px;}
  .expertise-list{position:absolute;left:352px;top:1846px;list-style:none;}
  .expertise-list li{position:relative;padding-left:40px;height:62px;line-height:40px;font-size:25px;white-space:nowrap;}
  .expertise-list li::before{content:"";position:absolute;left:0;top:13px;width:14px;height:14px;border-radius:50%;background:var(--heading-blue);}

  .site-footer{position:absolute;left:0;top:2312px;width:1200px;height:176px;background:var(--footer-blue);color:var(--white);}
  .footer-contact{position:absolute;left:132px;top:28px;font-size:24px;line-height:34px;white-space:nowrap;}
  .footer-cta{position:absolute;left:704px;top:22px;width:400px;text-align:center;font-family:"Raleway",sans-serif;}
  .footer-cta-title{font-size:40px;font-weight:400;}
  .footer-cta-link{font-size:30px;line-height:36px;color:var(--highlight-yellow);margin-top:2px;}
</style>
</head>
<body>
  <header class="site-header">
    <div class="brand-name">Kovrix.</div>
    <nav class="main-nav">
      <div class="nav-item is-active">What K do</div>
      <div class="nav-item">Who K are</div>
      <div class="nav-item">Why K</div>
    </nav>
  </header>

  <section class="hero">
    <div class="hero-visual" role="img" aria-label="Dark business photograph of a hand in a suit drawing glowing steps with a figure climbing them"></div>
    <p class="hero-tagline">Got momentum to make that leap into next level of business maturity?</p>
  </section>

  <section class="intro">
    <h1 class="section-title">Progress - Just in time.</h1>
    <div class="intro-body">
      <p class="intro-copy">Consultancy services aiming to help high-performing organizations adapt to change<br>&nbsp;and evolving economic conditions.</p>
      <p class="intro-copy">K delivers structure, means and orchestration to help growing companies develop healthy –<br>where in-house competencies or<br>bandwidth is simply not enough to implement a qualitative approach and lead on through.</p>
      <p class="intro-copy">In brief, an experienced trouble shooting asset when you need it.</p>
    </div>
  </section>

  <svg class="offer-corner" width="100" height="32" viewBox="0 0 100 32" aria-hidden="true">
    <polygon points="0,12 96,0 96,32 0,32" fill="#fbf22c"/>
  </svg>
  <aside class="offer-band">Growth plans? Download <a href="#">Kovrix's Kickstart offer [SWE]</a></aside>

  <section class="expertise">
    <h2 class="section-title">Areas we expertise</h2>
    <ul class="expertise-list">
      <li>Growth management</li>
      <li>Corporate communications</li>
      <li>Organizational development</li>
      <li>Gap analysis &amp; field research papers</li>
      <li>Project management</li>
      <li>Conceptualizing</li>
    </ul>
  </section>

  <footer class="site-footer">
    <div class="footer-contact">
      Kovrix © 2015 | Privacy Policy<br>
      T: +46 (0) 700 18 42 90<br>
      E: info@kovrix-demo.se
    </div>
    <div class="footer-cta">
      <div class="footer-cta-title">Get in touch!</div>
      <div class="footer-cta-link">Click here to<br>drop a mail to us</div>
    </div>
  </footer>
</body>
</html>
```